AV GLOSSUM BUSINESS CARD DESIGN PROJECT

We need to utilize our logo that was expertly created on Sketchloom and now need to match this with a business card design.

```html
<!DOCTYPE html>
<html lang="en">
<head>
<meta charset="utf-8">
<title>AV Glossum Business Card</title>
<link href="https://fonts.googleapis.com/css2?family=Montserrat:wght@400;500;700&display=swap" rel="stylesheet">
<style>
  :root {
    --stage: #2e2e2e;
    --card-black: #151515;
    --back-black: #121212;
    --back-mark: #2c2c2c;
    --white: #ffffff;
    --brand-blue: #0f51a8;
    --ink: #1c1c1c;
  }
  * { margin: 0; padding: 0; box-sizing: border-box; }
  html, body { width: 1200px; height: 689px; overflow: hidden; }
  body {
    background: var(--stage);
    font-family: "Montserrat", sans-serif;
    position: relative;
  }
  .card {
    position: absolute;
    top: 195px;
    width: 525px;
    height: 300px;
    border-radius: 24px;
    overflow: hidden;
  }
  .card-back { left: 45px; background: var(--back-black); }
  .card-front { left: 630px; background: var(--card-black); }

  .back-wordmark {
    position: absolute;
    inset: 0;
    display: flex;
    align-items: center;
    justify-content: center;
    font-weight: 700;
    font-size: 54px;
    letter-spacing: 4px;
    color: var(--back-mark);
  }

  .front-wave { position: absolute; inset: 0; }

  .front-wordmark {
    position: absolute;
    top: 26px;
    right: 60px;
    font-weight: 700;
    font-size: 26px;
    line-height: 32px;
    letter-spacing: 3px;
    color: var(--brand-blue);
  }

  .person { position: absolute; left: 42px; top: 192px; }
  .person-name {
    font-weight: 700;
    font-size: 20px;
    line-height: 24px;
    letter-spacing: 0.5px;
    color: var(--brand-blue);
  }
  .person-title {
    font-weight: 400;
    font-size: 13px;
    line-height: 16px;
    color: var(--ink);
    margin-top: 1px;
  }

  .contacts {
    position: absolute;
    left: 42px;
    top: 238px;
    list-style: none;
  }
  .contacts li {
    display: flex;
    align-items: center;
    gap: 8px;
    font-size: 12.5px;
    color: var(--ink);
    line-height: 17px;
  }
  .contacts svg { width: 11px; height: 11px; fill: var(--brand-blue); flex: none; }

  .address {
    position: absolute;
    right: 32px;
    top: 132px;
    text-align: right;
    font-size: 12.5px;
    line-height: 18px;
    color: var(--ink);
  }
</style>
</head>
<body>

  <section class="card card-back" aria-label="Card back">
    <div class="back-wordmark">AV GLOSSUM</div>
  </section>

  <section class="card card-front" aria-label="Card front">
    <svg class="front-wave" viewBox="0 0 525 300" preserveAspectRatio="none" aria-hidden="true">
      <path d="M0,186 C180,136 360,141 525,76 L525,300 L0,300 Z" fill="var(--white)"/>
      <path d="M0,166 C180,116 360,121 525,56" fill="none" stroke="var(--brand-blue)" stroke-width="6"/>
      <path d="M0,190 C180,140 360,145 525,80" fill="none" stroke="var(--brand-blue)" stroke-width="9"/>
    </svg>

    <div class="front-wordmark">AV GLOSSUM</div>

    <div class="person">
      <div class="person-name">MARCUS HALE</div>
      <div class="person-title">Managing Director</div>
    </div>

    <ul class="contacts">
      <li>
        <svg viewBox="0 0 24 24"><path d="M6.6 10.8a15 15 0 0 0 6.6 6.6l2.2-2.2a1 1 0 0 1 1-.25 11.4 11.4 0 0 0 3.6.57 1 1 0 0 1 1 1V20a1 1 0 0 1-1 1A17 17 0 0 1 3 4a1 1 0 0 1 1-1h3.5a1 1 0 0 1 1 1 11.4 11.4 0 0 0 .57 3.6 1 1 0 0 1-.25 1z"/></svg>
        123 456 789
      </li>
      <li>
        <svg viewBox="0 0 24 24"><path d="M2 5h20v14H2z M2 5l10 8 10-8" /></svg>
        info@yourgmail.com
      </li>
      <li>
        <svg viewBox="0 0 24 24"><circle cx="12" cy="12" r="10"/></svg>
        www.yourwebsite.com
      </li>
    </ul>

    <div class="address">Your address, City<br>State, Zip 1234</div>
  </section>

</body>
</html>
```